The Bayfield Wellness Clinic - Practice Flyer

We need a flyer that generally advertises our services. I've uploaded one old flyer as well as examples of others. I like the style of the materials made by this practice: https://www.facebook.com/PineRidgeCounselingHouse

```html
<!DOCTYPE html>
<html lang="en">
<head>
<meta charset="utf-8">
<title>The Bayfield Wellness Clinic – Practice Flyer</title>
<link rel="stylesheet" href="https://fonts.googleapis.com/css2?family=Cinzel:wght@400;600&family=Lato:wght@300;400;700&display=swap">
<style>
  :root {
    --olive: #979a61;
    --olive-light: #a3a26a;
    --forest: #2d3f2b;
    --ink: #3f3f3f;
    --muted: #5a5a5a;
    --white: #ffffff;
    --photo-a: #e9eef2;
    --photo-b: #c9d3d8;
  }
  * { margin: 0; padding: 0; box-sizing: border-box; }
  html, body { width: 855px; height: 1200px; overflow: hidden; background: var(--white); }
  .flyer {
    position: relative; width: 855px; height: 1200px; overflow: hidden;
    background: var(--white); font-family: "Lato", sans-serif; color: var(--ink);
  }
  .brand {
    position: absolute; left: 22px; top: 44px;
    font-family: "Cinzel", serif; font-weight: 600; font-size: 25px;
    color: var(--forest); letter-spacing: 0.5px; line-height: 1;
  }
  .website {
    position: absolute; right: 25px; top: 57px;
    font-size: 18px; font-weight: 400; letter-spacing: 0.6px; color: var(--ink);
  }
  .hero-photo {
    position: absolute; left: 0; top: 120px; width: 855px; height: 440px;
    background:
      linear-gradient(180deg, rgba(255,255,255,0.95) 0%, rgba(255,255,255,0) 45%),
      linear-gradient(100deg, #8fb0d6 0%, #d8c8a6 45%, #d9a260 58%, var(--photo-b) 80%, var(--photo-a) 100%);
  }
  .waves { position: absolute; left: 0; top: 0; width: 855px; height: 1200px; }
  .headline {
    position: absolute; left: 0; width: 855px; top: 565px; text-align: center;
    font-family: "Cinzel", serif; font-weight: 400; color: var(--white);
    font-size: 56px; line-height: 57px; letter-spacing: 1px;
  }
  .features {
    position: absolute; top: 764px; left: 0; width: 855px; height: 150px;
  }
  .feature {
    position: absolute; top: 0; width: 170px; margin-left: -85px; text-align: center;
  }
  .feature svg { display: block; margin: 0 auto; height: 70px; width: 70px; }
  .feature-label {
    margin-top: 13px; font-size: 17px; font-weight: 400; line-height: 22px;
    text-transform: uppercase; color: var(--ink);
  }
  .intro {
    position: absolute; top: 929px; left: 45px; width: 765px; text-align: center;
    font-size: 14.5px; font-weight: 300; line-height: 28px; color: var(--muted);
  }
  .contact-band {
    position: absolute; left: 0; top: 1015px; width: 855px; height: 185px;
    background: var(--olive); color: var(--white);
  }
  .location { position: absolute; top: 37px; }
  .location--first { left: 50px; }
  .location--second { left: 449px; }
  .location .pin { position: absolute; left: 0; top: 0; width: 28px; height: 36px; }
  .location .phone-icon { position: absolute; left: 0; top: 65px; width: 32px; height: 32px; }
  .location-name { position: absolute; left: 45px; top: 1px; font-size: 19.5px; font-weight: 700; white-space: nowrap; }
  .location-address { position: absolute; left: 45px; top: 31px; font-size: 16px; font-weight: 400; white-space: nowrap; }
  .location-phone { position: absolute; left: 45px; top: 70px; font-size: 22px; font-weight: 700; white-space: nowrap; }
</style>
</head>
<body>
<main class="flyer">
  <div class="brand">The Bayfield Wellness Clinic</div>
  <div class="website">www.bayfieldwellnessclinic.com</div>

  <div class="hero-photo" role="img" aria-label="Photo of a smiling couple seated on a sofa talking with a counselor in a bright room"></div>

  <svg class="waves" viewBox="0 0 855 1200" aria-hidden="true">
    <path d="M0,529 Q420,578 855,521 L855,724 Q427,682 0,724 Z" fill="var(--olive)"/>
    <path d="M365,551 Q640,545 855,484 L855,521 Q640,549 365,552 Z" fill="var(--forest)"/>
    <path d="M0,731 Q427,694 855,731 L855,756 Q427,702 0,756 Z" fill="var(--forest)"/>
  </svg>

  <h1 class="headline">The Bayfield<br>Wellness Clinic</h1>

  <section class="features">
    <div class="feature" style="left:92px">
      <svg viewBox="0 0 70 70" aria-hidden="true">
        <circle cx="44" cy="6" r="5" fill="var(--olive-light)"/>
        <path d="M37,13 h14 a4,4 0 0 1 4,4 v22 h-4 v28 h-5 v-24 h-4 v24 h-5 v-30 l-8,6 -3,-3 z" fill="var(--olive-light)"/>
        <circle cx="14" cy="25" r="4.5" fill="var(--forest)"/>
        <path d="M8,31 h12 a3,3 0 0 1 3,3 v16 h-3 v17 h-4 v-15 h-2 v15 h-4 v-17 h-3 v-16 a3,3 0 0 1 1,-3 z" fill="var(--forest)"/>
      </svg>
      <div class="feature-label">Serving<br>all ages</div>
    </div>
    <div class="feature" style="left:248px">
      <svg viewBox="0 0 70 70" aria-hidden="true">
        <rect x="13" y="6" width="44" height="60" rx="5" fill="none" stroke="var(--forest)" stroke-width="5"/>
        <rect x="25" y="1" width="20" height="8" rx="2" fill="var(--forest)"/>
        <rect x="21" y="16" width="28" height="40" fill="none" stroke="var(--forest)" stroke-width="3"/>
        <path d="M26,24 h18 M26,31 h18 M26,38 h18 M26,45 h10" stroke="var(--forest)" stroke-width="3"/>
      </svg>
      <div class="feature-label">Same day<br>appointments<br>available</div>
    </div>
    <div class="feature" style="left:417px">
      <svg viewBox="0 0 70 70" aria-hidden="true">
        <circle cx="49" cy="34" r="8" fill="var(--olive-light)"/>
        <path d="M40,44 h18 l8,12 v8 h-28 z" fill="var(--olive-light)"/>
        <circle cx="29" cy="26" r="11" fill="var(--forest)"/>
        <path d="M18,40 h22 l12,14 v10 h-46 v-10 z" fill="var(--forest)"/>
      </svg>
      <div class="feature-label">Accepting<br>new patients</div>
    </div>
    <div class="feature" style="left:581px">
      <svg viewBox="0 0 70 70" aria-hidden="true">
        <path d="M35,3 Q48,10 58,9 V38 Q58,56 35,67 Q12,56 12,38 V9 Q22,10 35,3 Z" fill="none" stroke="var(--forest)" stroke-width="5"/>
        <path d="M24,35 l8,9 l15,-18" fill="none" stroke="var(--olive-light)" stroke-width="6" stroke-linecap="round"/>
      </svg>
      <div class="feature-label">Accepts all<br>insurances</div>
    </div>
    <div class="feature" style="left:741px">
      <svg viewBox="0 0 70 70" aria-hidden="true">
        <path d="M40,24 a22,15 0 1 1 10,33 l8,6 -16,-4 a22,15 0 0 1 -2,-35 z" fill="var(--olive-light)"/>
        <ellipse cx="27" cy="26" rx="24" ry="16" fill="var(--white)" stroke="var(--forest)" stroke-width="5"/>
        <path d="M14,38 l-4,11 12,-7" fill="var(--white)" stroke="var(--forest)" stroke-width="4" stroke-linejoin="round"/>
      </svg>
      <div class="feature-label">No insurance?<br>We can help!</div>
    </div>
  </section>

  <p class="intro">Suspendisse magna nibh, molestie vitae interdum commodo, eleifend ac justo. In hac habitasse platea dictumst. Praesent semper, libero sed accumsan consectetur, orci nisl consectetur nisi, a auctor erat magna a justo.</p>

  <footer class="contact-band">
    <div class="location location--first">
      <svg class="pin" viewBox="0 0 28 36" aria-hidden="true">
        <path d="M14,34 C6,23 2,17 2,12 a12,12 0 0 1 24,0 c0,5 -4,11 -12,22 z" fill="none" stroke="var(--white)" stroke-width="1.6"/>
        <circle cx="14" cy="12" r="4" fill="none" stroke="var(--white)" stroke-width="1.6"/>
      </svg>
      <div class="location-name">Your location 1</div>
      <div class="location-address">Lorem Ipsum dolor 22, Suspende, FL 23901</div>
      <svg class="phone-icon" viewBox="0 0 32 32" aria-hidden="true">
        <path d="M7,2 l5,7 -3,4 c2,5 6,9 10,11 l4,-3 7,5 -3,4 c-11,1 -24,-12 -24,-24 z" fill="none" stroke="var(--white)" stroke-width="1.6" stroke-linejoin="round"/>
      </svg>
      <div class="location-phone">555.014.2290</div>
    </div>
    <div class="location location--second">
      <svg class="pin" viewBox="0 0 28 36" aria-hidden="true">
        <path d="M14,34 C6,23 2,17 2,12 a12,12 0 0 1 24,0 c0,5 -4,11 -12,22 z" fill="none" stroke="var(--white)" stroke-width="1.6"/>
        <circle cx="14" cy="12" r="4" fill="none" stroke="var(--white)" stroke-width="1.6"/>
      </svg>
      <div class="location-name">Your location 1</div>
      <div class="location-address">Lorem Ipsum dolor 22, Suspende, FL 23901</div>
      <svg class="phone-icon" viewBox="0 0 32 32" aria-hidden="true">
        <path d="M7,2 l5,7 -3,4 c2,5 6,9 10,11 l4,-3 7,5 -3,4 c-11,1 -24,-12 -24,-24 z" fill="none" stroke="var(--white)" stroke-width="1.6" stroke-linejoin="round"/>
      </svg>
      <div class="location-phone">555.014.2290</div>
    </div>
  </footer>
</main>
</body>
</html>
```